Flooring & Interior Design showroom

Just bought this business- Kestrel Lane Flooring & Interiors. Love our logo (we are on Kestrel Lane )and colors
Forest green, gold and black
Love that the back lists everything we do. We no longer have plenotilex but need to add in LVP/ SPC and need to take out vantor shadehub logo at the bottom and use the quib logo instead (maybe? open to suggestions)

Not in love with our cards- I want a higher end look
I hate the gradient poop color we have now.
Would love if they were all black - maybe or ??
or had a foil or embossing?

```html
<!DOCTYPE html>
<html lang="en">
<head>
<meta charset="utf-8">
<title>Kestrel Lane Flooring &amp; Interiors — Business Card</title>
<link href="https://fonts.googleapis.com/css2?family=Urbanist:wght@700&family=Barlow:wght@400;500;600&family=Heebo:wght@300&family=Montserrat:wght@700&display=swap" rel="stylesheet">
<style>
  :root{
    --page:#ffffff;
    --card-black:#1e1e1e;
    --card-deep:#111111;
    --card-lift:#2a2a2a;
    --ink:#ffffff;
    --ink-soft:#e9e9e9;
    --gold:#d8c98c;
    --forest:#1f5a3a;
    --shadow:rgba(0,0,0,.28);
  }
  html,body{margin:0;padding:0;width:1200px;height:1200px;overflow:hidden;background:var(--page);}
  p,h1,ul{margin:0;}
  .sheet{position:relative;width:1200px;height:1200px;}
  .card{position:absolute;width:911px;height:506px;color:var(--ink);box-shadow:6px 7px 6px var(--shadow);overflow:hidden;}
  .card--front{left:147px;top:57px;background:linear-gradient(200deg,var(--card-deep) 0%,#181818 45%,var(--card-lift) 100%);}
  .card--back{left:149px;top:643px;height:508px;background:var(--card-black);}

  /* brand wordmark */
  .brand{position:absolute;display:flex;align-items:center;gap:14px;}
  .brand__dot{width:34px;height:34px;border-radius:50%;background:var(--forest);flex:none;}
  .brand__name{font-family:"Barlow",sans-serif;font-weight:500;color:var(--gold);line-height:1.05;}
  .brand__name .line1{display:block;font-size:42px;letter-spacing:1px;}
  .brand__name .line2{display:block;font-size:17px;letter-spacing:2.6px;text-transform:uppercase;margin-top:6px;}
  .card--front .brand{left:48px;top:222px;}
  .card--back .brand{left:80px;top:125px;}

  /* front */
  .person{position:absolute;left:439px;top:96px;}
  .person__name{font-family:"Urbanist",sans-serif;font-weight:700;font-size:60px;line-height:1;letter-spacing:.5px;}
  .person__role{font-family:"Barlow",sans-serif;font-weight:400;font-size:29px;line-height:1.1;margin:0 0 0 1px;}
  .contact{position:absolute;left:434px;top:228px;padding:0;list-style:none;}
  .contact li{display:flex;align-items:center;height:38.8px;font-family:"Heebo",sans-serif;font-weight:300;font-size:22px;color:var(--ink-soft);white-space:nowrap;}
  .contact svg{width:22px;height:22px;fill:var(--ink);margin-right:20px;flex:none;}

  /* back */
  .tagline{position:absolute;left:80px;width:324px;top:234px;text-align:center;font-family:"Barlow",sans-serif;font-size:14.5px;line-height:1.2;letter-spacing:1px;color:var(--ink-soft);}
  .hotline{position:absolute;left:68px;top:302px;font-family:"Montserrat",sans-serif;font-weight:700;font-size:47px;letter-spacing:1px;line-height:1;white-space:nowrap;}
  .web{position:absolute;left:70px;top:354px;font-family:"Barlow",sans-serif;font-weight:500;font-size:19px;line-height:1.1;letter-spacing:2px;white-space:nowrap;}
  .services{position:absolute;top:44px;padding:0;list-style:none;}
  .services--a{left:456px;}
  .services--b{left:646px;}
  .services li{display:flex;align-items:center;height:33.8px;font-family:"Barlow",sans-serif;font-size:28px;white-space:nowrap;}
  .services li::before{content:"";width:0;height:0;border-top:6px solid transparent;border-bottom:6px solid transparent;border-left:10px solid var(--ink);margin-right:15px;}
  .partner{position:absolute;display:flex;align-items:center;gap:10px;font-family:"Barlow",sans-serif;font-weight:600;color:var(--ink);}
  .partner__mark{width:26px;height:26px;border-radius:50%;background:var(--ink);flex:none;}
  .partner--shades{left:452px;top:424px;font-size:27px;}
  .partner--reviews{left:690px;top:418px;font-size:38px;}
  .partner--reviews .partner__mark{width:22px;height:22px;}
</style>
</head>
<body>
<main class="sheet">

  <section class="card card--front" aria-label="Card front">
    <div class="brand">
      <span class="brand__dot"></span>
      <span class="brand__name"><span class="line1">Kestrel Lane</span><span class="line2">Flooring &amp; Interiors</span></span>
    </div>

    <div class="person">
      <h1 class="person__name">Mara Quillen</h1>
      <p class="person__role">Owner/ Designer</p>
    </div>

    <ul class="contact">
      <li><svg viewBox="0 0 24 24"><path d="M12 2a7 7 0 0 0-7 7c0 5 7 13 7 13s7-8 7-13a7 7 0 0 0-7-7zm0 9.5A2.5 2.5 0 1 1 12 6.5a2.5 2.5 0 0 1 0 5z"/></svg>314 Kestrel Lane, Cove Harbor CA 93900</li>
      <li><svg viewBox="0 0 24 24"><path d="M3 5h18v14H3zm1.5 1.6v1.2L12 12.5l7.5-4.7V6.6L12 11.2z"/></svg>tom@kestrellaneflooring.com</li>
      <li><svg viewBox="0 0 24 24"><path d="M9 16.2 4.8 12l-2.3 2.3L9 20.8 21.5 8.3 19.2 6z"/></svg>CA Lic # 418273</li>
      <li><svg viewBox="0 0 24 24"><path d="M3 4h18l1 5a3 3 0 0 1-3 2.5V20H5v-8.5A3 3 0 0 1 2 9zm4 10v4h4v-4zm6 0v6h4v-6z"/></svg>Store 555.214.0381</li>
      <li><svg viewBox="0 0 24 24"><path d="M7 1h10a2 2 0 0 1 2 2v18a2 2 0 0 1-2 2H7a2 2 0 0 1-2-2V3a2 2 0 0 1 2-2zm0 3v14h10V4zm5 15.5a1 1 0 1 0 0 2 1 1 0 0 0 0-2z"/></svg>Cell 555-786-0142</li>
      <li><svg viewBox="0 0 24 24"><path d="M6.6 10.8a15 15 0 0 0 6.6 6.6l2.2-2.2a1 1 0 0 1 1-.25 11.4 11.4 0 0 0 3.6.57 1 1 0 0 1 1 1V20a1 1 0 0 1-1 1A17 17 0 0 1 3 4a1 1 0 0 1 1-1h3.5a1 1 0 0 1 1 1c0 1.25.2 2.45.57 3.57a1 1 0 0 1-.25 1z"/></svg>Fax 555.647.0199</li>
    </ul>
  </section>

  <section class="card card--back" aria-label="Card back">
    <div class="brand">
      <span class="brand__dot"></span>
      <span class="brand__name"><span class="line1">Kestrel Lane</span><span class="line2">Flooring &amp; Interiors</span></span>
    </div>
    <p class="tagline">Home Town Service Since 1979</p>
    <p class="hotline">555.214.0381</p>
    <p class="web">www.kestrellaneflooring.com</p>

    <ul class="services services--a">
      <li>Area Rugs</li><li>Blinds</li><li>Carpet</li><li>Cork</li><li>Hardwood</li><li>Laminate</li><li>Sheers</li><li>Valances</li><li>Vinyl</li>
    </ul>
    <ul class="services services--b">
      <li>Bed Spreads</li><li>Draperies</li><li>LVP/ SPC</li><li>Fabric</li><li>Motorized Shades</li><li>Pillows</li><li>Shutters</li><li>Upholstery</li><li>Verticals</li>
    </ul>

    <div class="partner partner--shades"><span class="partner__mark"></span>Halden Shades</div>
    <div class="partner partner--reviews">quib<span class="partner__mark"></span></div>
  </section>

</main>
</body>
</html>
```